Advertising Portal Needs eBrochure

Hi Crowders! Our advertising portal, which focus on the new launches property, needs an online brochure to promote to potential advertisers the benefits of advertising their projects with us. These advertisers will be mainly real estate developers and agencies.

WHAT WE LOOKING FOR
We do not want over-fanciful designs that makes the content hard to read. The use of illustrations and graphics/symbols related to covered topics are encouraged. The overall design should portrait our advertising efficiency through online and social media means. Our website - www.brightkeyhomes.sg.

For draft purposes, just do up the front page, back page, and few inner pages, preferably to include one illustration chart (either on page 7/8). Size wise probably A5 portrait or landscape, for future printing into a booklet.

WORK COMPLETION AND PAYMENT
The $500 stated here is 50% of the payment. Upon getting a desired draft design, we will need you to work on the full content with slight amendments along the way. Once done, we will be paying the balance $500, and we will need the pdf file as well as the work file.

Let your design juice flow, and hope we can work with you!
Updates

Hi Crowders! Thank you for your submissions. We are closing the project as we've decided on a design. It's a pity we can only select one design, as there are a number of good works. Hope we will have a chance to work together on our upcoming projects. Cheers =)

Target Market(s)

Real estate developers, real estate agencies, and perhaps to an extent, individual property sales agent.

Industry/Entity Type

Advertising

Requirements
Should not have
• We prefer not to have much real people kind of stock images. Try not to use images from our portal as we do not have the ownerships. Instead, you can use stock images of property developments artist impression that gives a similar feel.

```html
<!DOCTYPE html>
<html lang="en">
<head>
<meta charset="UTF-8">
<title>Brochure Spread – Full-Featured Webpage</title>
<link href="https://fonts.googleapis.com/css2?family=Open+Sans:wght@400;600;700&display=swap" rel="stylesheet">
<style>
  :root {
    --olive: #a8b15d;
    --olive-deep: #9aa352;
    --ink: #1e1e1e;
    --paper: #ffffff;
    --sky-top: #6f9fd0;
    --sky-mid: #b9d3ea;
    --tower: #8a9aae;
    --foliage: #4f6a3a;
    --room-warm: #d9c7ad;
    --room-light: #e9e4dc;
  }
  html, body {
    margin: 0;
    padding: 0;
    overflow: hidden;
    background: var(--paper);
  }
  .spread {
    position: relative;
    width: 1200px;
    height: 423px;
    overflow: hidden;
    background: var(--paper);
    font-family: "Open Sans", Arial, sans-serif;
    color: var(--ink);
  }
  .band {
    position: absolute;
    background: var(--olive);
  }
  .band--top-left { left: 0; top: 15px; width: 602px; height: 74px; }
  .band--foot-left { left: 0; top: 403px; width: 602px; height: 20px; }
  .band--foot-right { left: 602px; top: 279px; width: 598px; height: 144px; }

  .title {
    position: absolute;
    left: 17px;
    top: 24px;
    margin: 0;
    font-size: 19.5px;
    line-height: 26px;
    font-weight: 700;
    color: var(--paper);
  }
  .body-copy {
    position: absolute;
    margin: 0;
    font-size: 11px;
    line-height: 15.2px;
    font-weight: 400;
  }
  .body-copy--intro { left: 17px; top: 96px; width: 440px; }
  .body-copy--impression { left: 17px; top: 267px; width: 270px; }
  .body-copy--details {
    left: 823px;
    top: 285px;
    width: 345px;
    color: var(--paper);
    line-height: 14.6px;
  }
  .subhead {
    position: absolute;
    margin: 0;
    color: var(--olive);
    font-weight: 600;
  }
  .subhead--impression { left: 17px; top: 206px; font-size: 19px; line-height: 25px; }
  .subhead--details { left: 639px; top: 35px; font-size: 17.5px; line-height: 24px; font-weight: 700; }

  .photo {
    position: absolute;
  }
  .photo--skyline {
    left: 465px;
    top: 55px;
    width: 735px;
    height: 224px;
    background: linear-gradient(180deg, var(--sky-top) 0%, var(--sky-mid) 45%, var(--tower) 80%, var(--foliage) 100%);
  }
  .photo--living {
    left: 299px;
    top: 212px;
    width: 135px;
    height: 113px;
    background: linear-gradient(135deg, var(--room-warm), var(--room-light));
  }
  .photo--kitchen {
    left: 362px;
    top: 297px;
    width: 142px;
    height: 108px;
    background: var(--paper);
    box-sizing: border-box;
    padding: 2px;
  }
  .photo--kitchen .photo-fill {
    width: 100%;
    height: 100%;
    background: linear-gradient(180deg, #d6d6d4, #b9b4ab);
  }
  .fold {
    position: absolute;
    left: 582px;
    top: 0;
    width: 40px;
    height: 423px;
    background: linear-gradient(90deg, rgba(0,0,0,0) 0%, rgba(0,0,0,0.10) 48%, rgba(0,0,0,0.04) 55%, rgba(0,0,0,0) 100%);
    pointer-events: none;
  }
</style>
</head>
<body>
<div class="spread">
  <!-- left page -->
  <div class="band band--top-left"></div>
  <h1 class="title">We Create A Full-Featured<br>Webpage For Your Project</h1>

  <p class="body-copy body-copy--intro">We treat your project as an accomplishment just as you see it.&nbsp; Your custom full-feature website reflects the hard work that you put into the project and the pride you feel at it's completion.&nbsp; These are not cut and paste one size fits all. We work closly with you to showcase specific aspects of the architecture that will make your building stand out.</p>

  <h2 class="subhead subhead--impression">Leave a lasting<br>impression</h2>
  <p class="body-copy body-copy--impression">The key to marketing is presentation...a professionally presented property provides buyers with a positive first impression which lasts.&nbsp; The presentation translates into positive feelings about your project helping convince them to investigate further.</p>

  <div class="photo photo--skyline" role="img" aria-label="City skyline of glass towers and a domed heritage building under a blue sky"></div>
  <div class="photo photo--living" role="img" aria-label="Bright furnished living room of a new apartment"></div>
  <div class="photo photo--kitchen"><div class="photo-fill" role="img" aria-label="Modern open kitchen with breakfast bar"></div></div>

  <div class="band band--foot-left"></div>

  <!-- right page -->
  <h2 class="subhead subhead--details">We handle all of the details.</h2>
  <div class="band band--foot-right"></div>
  <p class="body-copy body-copy--details">We employ a team of professional and experienced editors and designers that work tirelessly to produce a website that showcases your project.&nbsp; You simply provide the data and we do the rest.&nbsp; Once approved, your site immediately goes live to the buying public.&nbsp; We also offer unlimited updates as you get additional photos and details. You are assigned a project management single point of contact who knows your project in detail. This person then coordinates with the right people to make the changes you require.</p>

  <div class="fold"></div>
</div>
</body>
</html>
```